Established food business needs a new name card design

Refer to attached current name card. Would like a new professional look design with only the company name and logo without any pictures. Would like green and yellow to be included.
To include:
My name "HAKIM RUSLAN" and hand phone number "86207319".
To delete "
"Along Pinegrove Ave 3" and
"www.bu-tirah.com.sg"
To change email to:
"rvk27@tealmail.com.sg"

```html
<!DOCTYPE html>
<html lang="en">
<head>
<meta charset="utf-8">
<title>Bu-Tirah Eating Corner – Name Card</title>
<link rel="stylesheet" href="https://fonts.googleapis.com/css2?family=Roboto+Condensed:wght@700&family=Roboto:wght@400&display=swap">
<style>
  :root {
    --bg: #858585;
    --green: #0d4a30;
    --green-light: #10573a;
    --yellow: #f5cd14;
    --white: #ffffff;
    --contact: #e6ece8;
  }
  * { margin: 0; padding: 0; box-sizing: border-box; }
  html, body { width: 1200px; height: 900px; overflow: hidden; }
  body {
    background: radial-gradient(circle at 45% 40%, #9a9a9a, var(--bg) 70%);
    font-family: "Roboto", sans-serif;
    position: relative;
  }
  .card {
    position: absolute;
    top: 300px;
    width: 520px;
    height: 300px;
    overflow: hidden;
    box-shadow: 0 6px 18px rgba(0,0,0,0.35);
  }
  .card-front { left: 60px; background: var(--white); }
  .card-back {
    left: 620px;
    background: radial-gradient(circle at 40% 40%, var(--green-light), var(--green) 80%);
    display: flex;
    align-items: center;
    justify-content: center;
  }
  .card-waves { position: absolute; inset: 0; width: 520px; height: 300px; }
  .brand {
    position: absolute;
    display: flex;
    align-items: center;
    gap: 12px;
  }
  .brand-front { left: 150px; top: 30px; }
  .card-back .brand { position: static; gap: 18px; }
  .brand-dot {
    border-radius: 50%;
    background: var(--yellow);
  }
  .brand-front .brand-dot { width: 40px; height: 40px; }
  .card-back .brand-dot { width: 62px; height: 62px; }
  .brand-name {
    font-family: "Roboto Condensed", sans-serif;
    font-weight: 700;
    color: var(--yellow);
    letter-spacing: 1px;
  }
  .brand-front .brand-name { font-size: 34px; }
  .card-back .brand-name { font-size: 54px; }
  .holder-name {
    position: absolute;
    left: 22px;
    top: 212px;
    display: flex;
    align-items: center;
    gap: 8px;
    font-family: "Roboto Condensed", sans-serif;
    font-weight: 700;
    font-size: 21px;
    line-height: 24px;
    color: var(--yellow);
    letter-spacing: 0.5px;
  }
  .holder-name::before {
    content: "";
    width: 12px; height: 12px;
    border-radius: 50%;
    background: var(--yellow);
  }
  .contact-list {
    position: absolute;
    right: 18px;
    top: 216px;
    list-style: none;
    text-align: right;
    font-size: 11.5px;
    line-height: 16px;
    color: var(--contact);
  }
  .contact-list li { display: flex; justify-content: flex-end; align-items: center; gap: 6px; }
  .contact-icon {
    width: 12px; height: 12px;
    border-radius: 50%;
    background: var(--yellow);
    display: inline-flex; align-items: center; justify-content: center;
  }
  .contact-spacer { width: 12px; }
</style>
</head>
<body>
  <section class="card card-front">
    <svg class="card-waves" viewBox="0 0 520 300" aria-hidden="true">
      <path fill="var(--yellow)" d="M0 100 C180 190 380 210 520 170 L520 300 L0 300 Z"/>
      <path fill="var(--white)" d="M0 110 C180 200 380 220 520 180 L520 300 L0 300 Z"/>
      <path fill="var(--green)" d="M0 116 C180 206 380 226 520 186 L520 300 L0 300 Z"/>
    </svg>
    <div class="brand brand-front">
      <span class="brand-dot"></span>
      <span class="brand-name">BU-TIRAH</span>
    </div>
    <div class="holder-name">HAKIM RUSLAN</div>
    <ul class="contact-list">
      <li>18 Kranji Trade Park Lane 2<span class="contact-spacer"></span></li>
      <li># 02-07 Singapore 728154<span class="contact-spacer"></span></li>
      <li>86207319
        <span class="contact-icon"><svg width="8" height="8" viewBox="0 0 8 8"><path d="M1.5 1 L3 1 L3.5 2.6 L2.7 3.2 Q3.4 4.7 4.8 5.3 L5.4 4.5 L7 5 L7 6.5 Q3.5 7 1 2.5 Z" fill="var(--green)"/></svg></span>
      </li>
      <li>rvk27@tealmail.com.sg
        <span class="contact-icon"><svg width="8" height="8" viewBox="0 0 8 8"><rect x="1" y="2" width="6" height="4" fill="none" stroke="var(--green)" stroke-width="0.9"/><path d="M1 2 L4 4.4 L7 2" fill="none" stroke="var(--green)" stroke-width="0.9"/></svg></span>
      </li>
    </ul>
  </section>

  <section class="card card-back">
    <div class="brand">
      <span class="brand-dot"></span>
      <span class="brand-name">BU-TIRAH</span>
    </div>
  </section>
</body>
</html>
```